Package for Utensil Kit

we want to have a new design for our utensil kit, its a paper bag with both sides like files below. our website is www.peckbox.com and please use #FF6C0E as the main color and feel free to unleash your creativity.
the deadcut of the package is 14x26cm.pdf also showed the size.
in the front we want to show our band
in the back we need info list here:
1. www.peckbox.com and QR code
2.our locations (Now four) and phone number
3.other information needed

```html
<!DOCTYPE html>
<html lang="en">
<head>
<meta charset="utf-8">
<title>PeckBox Utensil Kit – Packets</title>
<link href="https://fonts.googleapis.com/css2?family=Montserrat:wght@600;800&display=swap" rel="stylesheet">
<style>
  :root {
    --stage: #d9d9d9;
    --paper: #f7f7f7;
    --brand: #ff6c0e;
    --brand-deep: #e8611a;
    --brand-soft: #f08150;
    --leaf-line: #e2e2e2;
    --leaf-fill: #cfcfcf;
    --seal: #dddddd;
    --ink-white: #ffffff;
  }
  * { box-sizing: border-box; margin: 0; padding: 0; }
  html, body { width: 1200px; height: 940px; overflow: hidden; background: var(--stage); }
  .canvas {
    position: relative;
    width: 1200px;
    height: 940px;
    overflow: hidden;
    background: var(--stage);
    font-family: "Montserrat", Arial, sans-serif;
  }
  .shared-defs { position: absolute; width: 0; height: 0; }
  .packet {
    position: absolute;
    width: 1000px;
    height: 240px;
  }
  .packet--back-row { left: 140px; top: 170px; }
  .packet--front-row { left: 60px; top: 500px; }
  .packet-shape { position: absolute; inset: 0; }
  .leaf-art {
    position: absolute;
    border-radius: 18px;
  }
  .leaf-art--left {
    left: 40px; top: 18px; width: 230px; height: 204px;
    background: linear-gradient(135deg, #ececec 0%, var(--leaf-line) 100%);
  }
  .leaf-art--right {
    left: 800px; top: 18px; width: 170px; height: 204px;
    background: linear-gradient(160deg, #dedede 0%, var(--leaf-fill) 100%);
  }
  .brand-lockup {
    position: absolute;
    left: 330px;
    top: 50px;
    color: var(--ink-white);
  }
  .brand-name {
    display: flex;
    align-items: center;
    gap: 12px;
    font-weight: 800;
    font-size: 84px;
    line-height: 1;
    letter-spacing: -1px;
  }
  .brand-dot {
    width: 20px; height: 20px;
    border-radius: 50%;
    background: var(--ink-white);
  }
  .brand-tagline {
    margin-top: 8px;
    font-weight: 800;
    font-size: 25px;
    letter-spacing: 2px;
  }
  .kit-label {
    position: absolute;
    left: 806px;
    top: 166px;
    color: var(--brand);
    font-weight: 800;
    font-size: 22px;
  }
</style>
</head>
<body>
<div class="canvas">
  <svg class="shared-defs" width="0" height="0" aria-hidden="true">
    <defs>
      <linearGradient id="paperGrad" x1="0" y1="0" x2="0" y2="1">
        <stop offset="0" stop-color="#ffffff"/>
        <stop offset="0.6" stop-color="#f6f6f6"/>
        <stop offset="1" stop-color="#e9e9e9"/>
      </linearGradient>
      <linearGradient id="bandGrad" x1="0" y1="0" x2="1" y2="1">
        <stop offset="0" stop-color="#e8611a"/>
        <stop offset="0.5" stop-color="#ff6c0e"/>
        <stop offset="1" stop-color="#f08150"/>
      </linearGradient>
      <pattern id="teethLeft" width="8" height="12" patternUnits="userSpaceOnUse">
        <path d="M0 0 L8 6 L0 12 Z" fill="#d9d9d9"/>
      </pattern>
      <pattern id="teethRight" x="992" width="8" height="12" patternUnits="userSpaceOnUse">
        <path d="M8 0 L0 6 L8 12 Z" fill="#d9d9d9"/>
      </pattern>
    </defs>
  </svg>

  <div class="packet packet--back-row">
    <svg class="packet-shape" width="1000" height="240" viewBox="0 0 1000 240">
      <rect x="0" y="0" width="1000" height="240" fill="url(#paperGrad)"/>
      <rect x="0" y="0" width="8" height="240" fill="url(#teethLeft)"/>
      <rect x="992" y="0" width="8" height="240" fill="url(#teethRight)"/>
      <g stroke="#dddddd" stroke-width="1.5">
        <line x1="22" y1="0" x2="22" y2="240"/><line x1="30" y1="0" x2="30" y2="240"/>
        <line x1="970" y1="0" x2="970" y2="240"/><line x1="978" y1="0" x2="978" y2="240"/>
      </g>
    </svg>
    <div class="leaf-art leaf-art--left" role="img" aria-label="Light grey line-drawn leaves and branch"></div>
    <div class="leaf-art leaf-art--right" role="img" aria-label="Grey tropical leaf pattern"></div>
    <svg class="packet-shape" width="1000" height="240" viewBox="0 0 1000 240">
      <path d="M320 36 C 410 16, 510 38, 600 28 C 680 18, 740 36, 770 64 C 790 94, 782 150, 772 176 C 752 218, 684 222, 604 214 C 504 206, 410 228, 320 208 C 282 198, 272 158, 274 120 C 276 82, 284 46, 320 36 Z" fill="url(#bandGrad)"/>
    </svg>
    <div class="brand-lockup">
      <div class="brand-name"><span>PeckBox</span><span class="brand-dot"></span></div>
      <div class="brand-tagline">HAINAN CHICKEN</div>
    </div>
    <div class="kit-label">Utensil Kit</div>
  </div>

  <div class="packet packet--front-row">
    <svg class="packet-shape" width="1000" height="240" viewBox="0 0 1000 240">
      <rect x="0" y="0" width="1000" height="240" fill="url(#paperGrad)"/>
      <rect x="0" y="0" width="8" height="240" fill="url(#teethLeft)"/>
      <rect x="992" y="0" width="8" height="240" fill="url(#teethRight)"/>
      <g stroke="#dddddd" stroke-width="1.5">
        <line x1="22" y1="0" x2="22" y2="240"/><line x1="30" y1="0" x2="30" y2="240"/>
        <line x1="970" y1="0" x2="970" y2="240"/><line x1="978" y1="0" x2="978" y2="240"/>
      </g>
    </svg>
    <div class="leaf-art leaf-art--left" role="img" aria-label="Light grey line-drawn leaves and branch"></div>
    <div class="leaf-art leaf-art--right" role="img" aria-label="Grey tropical leaf pattern"></div>
    <svg class="packet-shape" width="1000" height="240" viewBox="0 0 1000 240">
      <path d="M320 36 C 410 16, 510 38, 600 28 C 680 18, 740 36, 770 64 C 790 94, 782 150, 772 176 C 752 218, 684 222, 604 214 C 504 206, 410 228, 320 208 C 282 198, 272 158, 274 120 C 276 82, 284 46, 320 36 Z" fill="url(#bandGrad)"/>
    </svg>
    <div class="brand-lockup">
      <div class="brand-name"><span>PeckBox</span><span class="brand-dot"></span></div>
      <div class="brand-tagline">HAINAN CHICKEN</div>
    </div>
    <div class="kit-label">Utensil Kit</div>
  </div>
</div>
</body>
</html>
```